Business card design for holistic health care clinic

We need a double-sided business card design for our holistic health care clinic that integrates our logo design and also its color scheme. My business is called Veluma. It is an integrative medicine clinic. You have already done the logo for me. Please ensure an elegant and upscale design that is not cluttered, but still has all the necessary information (please see below for details).

Target Market(s)

Wellness, fitness, rehabilitation for educated, well-traveled open-minded clients who are focused on natural, organic, balanced and preventive healthcare and lifestyle.

Industry/Entity Type

Medical

Contact Information for Business Card

Modern, clean.

Number of Pages Required

1 page

Font styles to use
Serif
Sans Serif

Colors

Designer to choose colors to be used in the design.

Requirements
Must have
• Logo on one side, all other information on the other side.
• Other information should include:
• Tomas Brevik - DOE, CPT, LMT
• 4120 North Harlow Street
• Austin, TX 78631
• 512 608 2947
• 818 459 7208
• info@VelumaHealth.com
• t.brevik@VelumaHealth.com
Nice to have
• Darker background on front - but not totally black - shaded/dark gray.

```html
<!DOCTYPE html>
<html lang="en">
<head>
<meta charset="utf-8">
<title>Veluma – Business Card</title>
<link rel="stylesheet" href="https://fonts.googleapis.com/css2?family=Source+Sans+3:wght@400;600;700&display=swap">
<style>
  :root {
    --canvas-bg: #e6e8eb;
    --card-bg: #f7f7f5;
    --brand-blue: #1a8fcf;
    --ink: #2b2b2b;
    --on-blue: #ffffff;
    --art-tone: #f3f6f8;
  }
  * { box-sizing: border-box; margin: 0; padding: 0; }
  html, body {
    width: 1200px; height: 900px; overflow: hidden;
    background: var(--canvas-bg);
    font-family: "Source Sans 3", "Helvetica Neue", Arial, sans-serif;
  }
  .card {
    position: absolute; left: 80px; top: 130px;
    width: 1040px; height: 640px;
    background: var(--card-bg);
    overflow: hidden;
    box-shadow: 0 10px 30px rgba(0,0,0,0.12);
  }
  .holder { position: absolute; left: 59px; top: 78px; display: flex; align-items: baseline; gap: 20px; }
  .holder__name { font-weight: 700; font-size: 33px; color: var(--brand-blue); letter-spacing: 0.5px; }
  .holder__credentials { font-weight: 400; font-size: 25px; color: var(--ink); }
  .brand {
    position: absolute; left: 531px; top: 150px; width: 460px;
    text-align: center;
    font-weight: 700; font-size: 104px; line-height: 1;
    color: var(--brand-blue); letter-spacing: 2px;
  }
  .contacts { position: absolute; left: 59px; top: 238px; list-style: none; }
  .contacts li {
    display: flex; align-items: center; gap: 14px;
    font-size: 27px; line-height: 38px; color: var(--ink);
  }
  .contacts svg { width: 22px; height: 22px; fill: var(--brand-blue); flex: none; }
  .wave { position: absolute; left: 0; top: 0; width: 1040px; height: 640px; }
  .address {
    position: absolute; left: 72px; top: 540px;
    font-size: 27px; color: var(--on-blue);
  }
</style>
</head>
<body>
  <main class="card">
    <svg class="wave" viewBox="0 0 1040 640" aria-hidden="true">
      <path fill="var(--brand-blue)" d="M0 425 C60 440 120 475 200 470 C290 464 360 430 440 428 C560 425 640 420 740 400 C850 378 950 390 1040 420 L1040 640 L0 640 Z"/>
      <rect x="771" y="379" width="240" height="256" rx="60" fill="var(--art-tone)" role="img" aria-label="Decorative bone illustration in white on the blue band"/>
    </svg>

    <div class="holder">
      <span class="holder__name">TOMAS BREVIK</span>
      <span class="holder__credentials">DOE, CPT, LMT</span>
    </div>

    <div class="brand">VELUMA</div>

    <ul class="contacts">
      <li><svg viewBox="0 0 24 24"><path d="M3 9c0-3 4-5 9-5s9 2 9 5l-4 1-1-3H8L7 10 3 9zm3 3h12l2 8H4l2-8zm6 2a2.5 2.5 0 100 5 2.5 2.5 0 000-5z"/></svg>512 608 2947</li>
      <li><svg viewBox="0 0 24 24"><path d="M7 2h10a1 1 0 011 1v18a1 1 0 01-1 1H7a1 1 0 01-1-1V3a1 1 0 011-1zm1 3v13h8V5H8zm4 14.5a1 1 0 100 2 1 1 0 000-2z"/></svg>818 459 7208</li>
      <li><svg viewBox="0 0 24 24"><path d="M2 5h20v14H2V5zm2 2v.5l8 5.5 8-5.5V7l-8 5.5L4 7z"/></svg>info@VelumaHealth.com</li>
      <li><svg viewBox="0 0 24 24"><path d="M2 5h20v14H2V5zm2 2v.5l8 5.5 8-5.5V7l-8 5.5L4 7z"/></svg>t.brevik@VelumaHealth.com</li>
      <li><svg viewBox="0 0 24 24"><path d="M12 2a10 10 0 100 20 10 10 0 000-20zm-1 3c-1 2-3 2-3 4s2 2 3 3-1 3 0 5c-4-1-6-4-6-7s3-5 6-5zm3 0c3 1 5 4 5 7 0 2-1 4-3 5 0-2 1-3 0-4s-3 0-3-2 2-2 1-6z"/></svg>www.VelumaHealth.com</li>
    </ul>

    <p class="address">4120 North Harlow Street Austin, TX 78631</p>
  </main>
</body>
</html>
```